Stylish Homeware business needs a Logo and Business Card design

We need a logo and business card for a new company based in Hong Kong called "Nest Avenue". We do marketing and distributing international stylish Homeware brands in Asia. Products we handle included clocks, picture frame, small kitchen wares, LED lightenings, stationary and etc. We planned to also create our own brands next step. We could like to see designs that use pastel colors. The final design shoudl be simple and stylish.
Target Market(s)
Asia, Mainly Japan, China and Korea
Industry/Entity Type
Business
Contact Information for Business Card
We could like to see designs that use pastel colors. The final design shoudl be simple and stylish. We attach some log design we like on the bottom of the page.
Look and feel
Each slider illustrates characteristics of the customer's brand and the style your logo design should communicate.

```html
<!DOCTYPE html>
<html lang="en">
<head>
<meta charset="utf-8">
<title>Nest Avenue — Business Card</title>
<link href="https://fonts.googleapis.com/css2?family=Open+Sans:wght@300;400;700&family=Lora:wght@400&display=swap" rel="stylesheet">
<style>
  :root {
    --page-bg: #f4f5f5;
    --teal: #73b8bf;
    --teal-light: #7cc3ca;
    --card-white: #f1f1f1;
    --ink: #6b6b6b;
    --ink-dark: #5a5a5a;
    --logo-white: #f4fafb;
  }
  * { margin: 0; padding: 0; box-sizing: border-box; }
  html, body {
    width: 1200px;
    height: 900px;
    overflow: hidden;
    background: var(--page-bg);
    font-family: "Open Sans", sans-serif;
  }
  .canvas {
    position: relative;
    width: 1200px;
    height: 900px;
  }
  .card {
    position: absolute;
    width: 640px;
    height: 366px;
    border-radius: 26px;
    box-shadow: 0 6px 18px rgba(0,0,0,0.18);
  }
  /* Front card */
  .card-front {
    left: 110px;
    top: 70px;
    background: linear-gradient(90deg, var(--teal-light), var(--teal));
    display: flex;
    align-items: center;
    justify-content: center;
  }
  .brand-front {
    display: flex;
    align-items: center;
    gap: 16px;
    color: var(--logo-white);
    font-size: 22px;
    font-weight: 400;
    letter-spacing: 0.42em;
    text-transform: uppercase;
  }
  .brand-square {
    width: 26px;
    height: 26px;
    background: var(--logo-white);
  }
  /* Back card */
  .card-back {
    left: 450px;
    top: 470px;
    background: linear-gradient(100deg, #ffffff, var(--card-white) 60%, #e8e8e8);
    display: flex;
    align-items: center;
  }
  .brand-back {
    width: 330px;
    display: flex;
    flex-direction: column;
    align-items: center;
    gap: 18px;
    color: var(--teal);
    font-size: 19px;
    font-weight: 400;
    letter-spacing: 0.4em;
    text-transform: uppercase;
  }
  .brand-back .brand-square {
    width: 70px;
    height: 70px;
    background: var(--teal);
  }
  .divider {
    width: 2px;
    height: 200px;
    background: var(--teal);
  }
  .contact {
    padding-left: 32px;
  }
  .person-name {
    font-size: 26px;
    font-weight: 300;
    color: var(--ink);
    line-height: 1.1;
  }
  .person-name strong { font-weight: 700; color: var(--ink-dark); }
  .job-title {
    font-family: "Lora", serif;
    font-size: 19px;
    color: var(--teal);
    margin: 2px 0 16px 14px;
  }
  .contact-list {
    list-style: none;
    margin-left: 30px;
  }
  .contact-list li {
    display: flex;
    align-items: center;
    gap: 12px;
    font-size: 15px;
    color: var(--ink);
    margin-bottom: 6px;
  }
  .contact-list svg {
    width: 16px;
    height: 16px;
    flex: none;
  }
</style>
</head>
<body>
<main class="canvas">
  <section class="card card-front">
    <div class="brand-front">
      <span class="brand-square"></span>
      <span class="brand-name">Nest Avenue</span>
    </div>
  </section>

  <section class="card card-back">
    <div class="brand-back">
      <span class="brand-square"></span>
      <span class="brand-name">Nest Avenue</span>
    </div>
    <div class="divider"></div>
    <div class="contact">
      <p class="person-name">Your <strong>Name</strong></p>
      <p class="job-title">Job Title</p>
      <ul class="contact-list">
        <li>
          <svg viewBox="0 0 16 16" aria-hidden="true"><path d="M8 1a5 5 0 0 0-5 5c0 3.8 5 9 5 9s5-5.2 5-9a5 5 0 0 0-5-5zm0 7a2 2 0 1 1 0-4 2 2 0 0 1 0 4z" fill="#73b8bf"/></svg>
          your address
        </li>
        <li>
          <svg viewBox="0 0 16 16" aria-hidden="true"><path d="M2 6c0-2 3-3 6-3s6 1 6 3v1h-3V5.5H5V7H2zM4 8h8l2 6H2z" fill="#73b8bf"/><circle cx="8" cy="11" r="1.6" fill="#fff"/></svg>
          000 000 0000
        </li>
        <li>
          <svg viewBox="0 0 16 16" aria-hidden="true"><g fill="none" stroke="#73b8bf" stroke-width="1.2"><circle cx="8" cy="8" r="6.5"/><ellipse cx="8" cy="8" rx="3" ry="6.5"/><path d="M1.5 8h13M2.5 5h11M2.5 11h11"/></g></svg>
          youremail@xyz.com
        </li>
      </ul>
    </div>
  </section>
</main>
</body>
</html>
```